Business card design and logo needed - Photographer

I take photos of weddings, rodeos, snowmobiling.
Need a card to hand out to prospective clients.
Industry/Entity Type
Business
Contact Information for Business Card
Marcus Dolven Photography
Requirements
Must have
- Bold
Black or white base.
My website. www.MarcusDolven.example
Should not have
- camera/ lens/ aperture blades

```html
<!DOCTYPE html>
<html lang="en">
<head>
<meta charset="utf-8">
<title>Marcus Dolven Photography – Business Card</title>
<link rel="stylesheet" href="https://fonts.googleapis.com/css2?family=Libre+Baskerville&family=Raleway:wght@300&family=Pathway+Gothic+One&display=swap">
<style>
  :root {
    --backdrop: #c9cacc;
    --card: #f7f7f6;
    --ink: #2f3439;
    --ink-soft: #5a5e63;
    --pattern-tone: #e4e5e6;
  }
  * { box-sizing: border-box; margin: 0; padding: 0; }
  html, body { width: 1200px; height: 800px; overflow: hidden; }
  body {
    background: var(--backdrop);
    display: flex;
    align-items: center;
    justify-content: center;
    gap: 40px;
  }
  .card {
    width: 520px;
    height: 297px;
    background: var(--card);
    box-shadow: 0 4px 14px rgba(0,0,0,0.18);
    position: relative;
  }
  .card-back__pattern {
    position: absolute;
    inset: 0;
    background: linear-gradient(135deg, var(--pattern-tone), #dcdddf);
  }
  .card-front {
    display: flex;
    flex-direction: column;
    align-items: center;
    padding-top: 44px;
  }
  .brand-mark {
    width: 84px;
    height: 84px;
    border-radius: 50%;
    background: var(--ink);
  }
  .brand-name {
    margin-top: 16px;
    font-family: "Libre Baskerville", serif;
    font-size: 28px;
    letter-spacing: 0.5px;
    color: var(--ink);
    text-transform: uppercase;
    line-height: 1;
  }
  .brand-tagline {
    margin-top: 6px;
    font-family: "Raleway", sans-serif;
    font-weight: 300;
    font-size: 13px;
    letter-spacing: 6px;
    color: var(--ink-soft);
    text-transform: uppercase;
  }
  .contact-list {
    position: absolute;
    bottom: 26px;
    left: 0;
    right: 0;
    display: flex;
    justify-content: center;
    gap: 18px;
    list-style: none;
  }
  .contact-item {
    display: flex;
    align-items: center;
    gap: 6px;
    font-family: "Pathway Gothic One", sans-serif;
    font-size: 13px;
    letter-spacing: 0.3px;
    color: var(--ink-soft);
    text-transform: uppercase;
  }
  .contact-label {
    width: 18px;
    height: 18px;
    border-radius: 50%;
    background: var(--ink);
    color: var(--card);
    font-size: 12px;
    display: flex;
    align-items: center;
    justify-content: center;
  }
</style>
</head>
<body>
  <section class="card card-back">
    <div class="card-back__pattern" role="img" aria-label="Repeating pattern of the brand monogram on a light grey field"></div>
  </section>

  <section class="card card-front">
    <div class="brand-mark" aria-hidden="true"></div>
    <h1 class="brand-name">Marcus Dolven</h1>
    <p class="brand-tagline">Photography</p>
    <ul class="contact-list">
      <li class="contact-item"><span class="contact-label">T</span>306 555 0142</li>
      <li class="contact-item"><span class="contact-label">E</span>marcusdolven@mail.example</li>
      <li class="contact-item"><span class="contact-label">W</span>www.MarcusDolven.example</li>
    </ul>
  </section>
</body>
</html>
```